Business Card Design Project

KB Consulting Associates is a management consulting business with C-suite (CEO/CFO etc) target clients. Logo selected is blue with simple/serious typefaces.

Target Market(s)

CEOs and CFOs of large corporates

Industry/Entity Type

Management Consulting

Font styles to use
Serif

Colors
3276b5

Requirements
Must have
• Tag line: Building successful collaborations (use different font)
Address: 427 Fernvale Crescent #03-22 Singapore 519337
Telephone: +65 8372 4096
Email: kbloh@postnest42.com

```html
<!DOCTYPE html>
<html lang="en">
<head>
<meta charset="utf-8">
<title>KB Consulting Associates – Business Card</title>
<link rel="stylesheet" href="https://fonts.googleapis.com/css2?family=Quicksand:wght@400;500;700&display=swap">
<style>
  :root {
    --frame: #1a5c9a;
    --navy-pattern: #12263a;
    --navy: #00243a;
    --sky: #00a0e0;
    --brand-blue: #1fa6e2;
    --white: #ffffff;
    --rule: #1b2f6e;
    --rule-soft: #c9d2dc;
  }
  * { margin: 0; padding: 0; box-sizing: border-box; }
  html, body { width: 1200px; height: 1017px; overflow: hidden; background: var(--white); }
  .canvas {
    position: relative; width: 1200px; height: 1017px;
    border: 3px solid var(--frame); background: var(--white);
    font-family: "Quicksand", sans-serif;
  }
  .card { position: absolute; overflow: hidden; }
  .card-front { left: 185px; top: 351px; width: 422px; height: 263px; }
  .card-back  { left: 641px; top: 355px; width: 395px; height: 261px; }
  .card-top, .card-bottom { position: absolute; left: 0; width: 100%; }
  .card-front .card-top { top: 0; height: 156px; background: var(--navy-pattern); }
  .card-front .card-bottom { top: 156px; bottom: 0; background: var(--sky); }
  .card-back .card-top { top: 0; height: 154px; background: var(--navy); }
  .card-back .card-bottom { top: 154px; bottom: 0; background: var(--sky); }

  .brand-name {
    position: absolute; left: 0; right: 0; top: 82px;
    text-align: center; font-weight: 700; font-size: 27px;
    color: var(--brand-blue); letter-spacing: 0.2px;
  }
  .tagline-block { position: absolute; left: 50px; top: 22px; width: 315px; height: 44px; }
  .tagline-rules { position: absolute; left: 0; top: 0; }
  .tagline {
    position: absolute; left: 0; right: 0; top: 10px;
    text-align: center; font-size: 18.5px; font-weight: 400; line-height: 24px;
    color: var(--white); letter-spacing: -0.3px; white-space: nowrap;
  }

  .contact-block {
    position: absolute; left: 63px; top: 54px;
    border-left: 2px solid var(--rule-soft); padding-left: 9px;
    color: var(--white); font-size: 17.5px; font-weight: 500; line-height: 23.5px;
    font-style: normal;
  }
  .email {
    position: absolute; left: 0; right: 0; top: 40px;
    text-align: center; color: var(--white); font-size: 18.5px; font-weight: 500;
  }
</style>
</head>
<body>
<main class="canvas">
  <section class="card card-front">
    <div class="card-top" role="img" aria-label="Dark navy zigzag background pattern"></div>
    <div class="brand-name">KB Consulting Associates</div>
    <div class="card-bottom">
      <div class="tagline-block">
        <svg class="tagline-rules" width="315" height="44" viewBox="0 0 315 44" aria-hidden="true">
          <g stroke="#1b2f6e" stroke-width="1.5">
            <line x1="1" y1="7" x2="139" y2="7"/><line x1="176" y1="7" x2="314" y2="7"/>
            <line x1="1" y1="39" x2="139" y2="39"/><line x1="176" y1="39" x2="314" y2="39"/>
          </g>
          <g fill="#1b2f6e" font-size="10" font-family="sans-serif" text-anchor="middle">
            <text x="157.5" y="11">★★★</text>
            <text x="157.5" y="43">★★★</text>
          </g>
        </svg>
        <p class="tagline">Building successful collaborations</p>
      </div>
    </div>
  </section>

  <section class="card card-back">
    <div class="card-top">
      <address class="contact-block">
        427 Fernvale<br>
        Crescent #03-22 Singapore 519337<br>
        Telephone: +65 8372 4096
      </address>
    </div>
    <div class="card-bottom">
      <p class="email">Email: kbloh@postnest42.com</p>
    </div>
  </section>
</main>
</body>
</html>
```